Landing-Page-Design für Immobilienunternehmen
Zielgruppe
Die Firma Halvak Immobilien kauft jegliche Art von Immobilien im Osten von Hamburg. Die Zielgruppe sind Immobilienbesitzer, welche ihre Wohnung, Haus, Gewerbe oder Sonstiges verkaufen möchten/müssen.
Ich würde gerne drei Unterzielgruppe mehr ansprechen:
Verkauf weil geerbt
textlich untermauert
Verkauf weil ins Altersheim
Verkauf weil ein Geldengpass
Wir kaufen:
Häuser
Eigentumswohnungen
Gewerbeflächen
Mehrfamilienhäuser
Garagen
Agrarflächen (Wald, Acker, Wiese, Teiche)
Aufgabenstellung
Es besteht ein Logo, welches berücksichtigt werden müsste.
Außerdem:
- responsive
- seriös
- conversion optimiert
- viel bebildert, textliche untermauert
- vertrauensvoll/verschwiegen
Telefonnummer soll prominent dargestellt werden, genauso wie ein Kontaktformular.

```html
<!DOCTYPE html>
<html lang="de">
<head>
<meta charset="utf-8">
<title>Halvak Immobilien – Wir kaufen Ihre Immobilie</title>
<link href="https://fonts.googleapis.com/css2?family=Roboto:wght@400;500;700&family=Saira+Condensed:wght@500&display=swap" rel="stylesheet">
<style>
:root{
  --ink:#2b3740;
  --green:#7cb518;
  --white:#ffffff;
  --card:#f2f2f2;
  --line:#2b3740;
  --photo-a:#eef1f3;
  --photo-b:#c9c3bb;
}
*{box-sizing:border-box;margin:0;padding:0}
html,body{width:1200px;height:2417px;overflow:hidden}
body{position:relative;background:var(--white);font-family:"Roboto",sans-serif;color:var(--ink)}
.abs{position:absolute}
.hero-photo{left:0;top:0;width:1200px;height:638px;background:linear-gradient(110deg,var(--photo-a) 0%,#dcdad6 45%,var(--photo-b) 100%)}
.brand{left:0;top:86px;width:1200px;text-align:center}
.brand-name{font-weight:700;font-size:24px;letter-spacing:.5px;color:var(--ink)}
.brand-name::before{content:"";display:inline-block;width:14px;height:14px;background:var(--green);margin-right:9px;vertical-align:1px}
.brand-tag{font-size:10px;letter-spacing:.6px;color:var(--ink);margin-top:3px}
.band{left:0;top:638px;width:1200px;height:658px;background:var(--ink)}
.hero-shape{left:0;top:0}
.hero-title{left:203px;top:482px;font-size:50px;line-height:51px;font-weight:400;color:var(--green);z-index:2}
.hotline{left:128px;top:617px;font-size:24px;line-height:30px;color:var(--white);z-index:2}
.quick{width:70px;height:65px;background:var(--ink);left:1092px;display:flex;align-items:center;justify-content:center}
.type{top:698px;width:170px;margin-left:-85px;text-align:center;color:var(--white);font-size:18px}
.type svg{display:block;margin:0 auto 4px}
.card{top:833px;width:307px;height:384px;background:var(--card);text-align:center;overflow:hidden}
.card-visual{width:120px;height:98px;margin:10px auto 0;background:#dcdcdc;border-radius:6px}
.card h3{color:var(--green);font-size:23px;line-height:34px;font-weight:700;margin-top:8px;height:86px;white-space:nowrap}
.card p{text-align:left;font-size:23px;line-height:33px;padding:0 12px 0 19px;letter-spacing:-.1px}
.cta-shape{left:0;top:1295px}
.cta-title{left:695px;top:1293px;font-size:52px;line-height:52px;color:var(--white);font-weight:400}
.intro{left:707px;top:1500px;width:390px;font-size:15px;line-height:21px}
.map{left:198px;top:1617px;width:295px;height:324px;border:2px solid var(--line);background:#f5f5f5}
.address{left:198px;top:1975px;font-size:15px;line-height:21px;font-style:normal}
.form{left:661px;top:1606px;width:434px}
.field{border:2px solid var(--line);border-radius:0;height:47px;margin-bottom:23px;padding:0 14px}
.field.tall{height:137px}
.field legend{font-family:"Saira Condensed",sans-serif;font-size:11px;letter-spacing:2.6px;padding:0 8px;margin-left:12px;text-transform:uppercase;font-weight:500}
.consent{font-size:13px;line-height:21px;letter-spacing:.4px;margin-top:-4px}
.submit{display:block;width:433px;height:52px;margin-top:23px;background:var(--green);color:var(--white);border:0;font-family:"Roboto",sans-serif;font-size:20px;letter-spacing:3px}
.footer{left:0;top:2312px;width:1200px;height:105px;background:var(--ink);color:var(--white);font-size:16px}
.footer nav{position:absolute;left:200px;top:29px;display:flex;gap:23px}
.footer a{color:var(--white);text-decoration:none}
.copy{position:absolute;right:104px;top:29px;font-size:15px}
</style>
</head>
<body>

<div class="abs hero-photo" role="img" aria-label="Foto: Berater im Gespräch mit einem älteren Ehepaar am Tisch"></div>
<section class="abs band"></section>

<div class="abs brand">
  <div class="brand-name">HALVAK IMMOBILIEN</div>
  <div class="brand-tag">VERWALTUNG · BERATUNG · INVESTMENT</div>
</div>

<svg class="abs hero-shape" width="1200" height="640" aria-hidden="true">
  <polygon points="0,640 169,451 492,451 670,640" fill="#2b3740"/>
</svg>
<h1 class="abs hero-title">Wir kaufen<br>Ihre Immobilie.</h1>
<p class="abs hotline">Kostenlose Service-Hotline: 0800 418 27 90</p>

<a class="abs quick" style="top:402px" aria-label="Anrufen">
  <svg width="40" height="40" viewBox="0 0 24 24" fill="none" stroke="#7cb518" stroke-width="1.3"><path d="M5 3h4l2 5-2.5 1.5a11 11 0 0 0 6 6L16 13l5 2v4a2 2 0 0 1-2 2A17 17 0 0 1 3 5a2 2 0 0 1 2-2z"/></svg>
</a>
<a class="abs quick" style="top:482px" aria-label="Nachricht senden">
  <svg width="42" height="40" viewBox="0 0 24 24" fill="none" stroke="#7cb518" stroke-width="1.3"><path d="M3 4h18v12H9l-5 4v-4H3z"/></svg>
</a>

<div class="abs type" style="left:187px">
  <svg width="108" height="50" viewBox="0 0 108 50" fill="none" stroke="#fff" stroke-width="2"><path d="M2 48h104M14 48V24L42 6l28 18v24M70 30h20l10 10v8M36 48V32h14v16M36 38h14"/></svg>Haus</div>
<div class="abs type" style="left:395px">
  <svg width="96" height="58" viewBox="0 0 96 58" fill="none" stroke="#fff" stroke-width="2"><path d="M0 56h96M16 56V2h64v54M24 12h12v8H24zM42 12h12v8H42zM60 12h12v8H60zM24 28h12v8H24zM42 28h12v8H42zM60 28h12v8H60zM42 44h12v12"/></svg>Wohnung</div>
<div class="abs type" style="left:605px">
  <svg width="100" height="60" viewBox="0 0 100 60" fill="none" stroke="#fff" stroke-width="2"><path d="M0 58h100M16 58V2h70v56M16 20l28-10v48M44 26l22-8v40M28 58V42h10v16M58 58V42h10v16"/></svg>Gewerbeflächen</div>
<div class="abs type" style="left:803px">
  <svg width="110" height="40" viewBox="0 0 110 40" fill="none" stroke="#fff" stroke-width="2"><path d="M0 38h110M32 38V18l24-10 24 10v20M42 38V24h28v14"/></svg>Garage</div>
<div class="abs type" style="left:1006px">
  <svg width="100" height="54" viewBox="0 0 100 54" fill="none" stroke="#fff" stroke-width="2"><path d="M4 52h92M38 52V30M38 30c-10 0-10-26 0-26s10 26 0 26zM18 52V40a6 6 0 0 1 12 0v12M52 44h42v8"/></svg>Agrarflächen</div>

<article class="abs card" style="left:97px">
  <div class="card-visual" role="img" aria-label="Illustration: Hand trägt ein Haus"></div>
  <h3>Immobilien Erbschaft</h3>
  <p>Erfolgreich die geerbte Immobilie verkaufen? Mit einem zuverlässigen Partner an der Seite geht es leichter.</p>
</article>
<article class="abs card" style="left:444px">
  <div class="card-visual" role="img" aria-label="Illustration: Sparschwein mit Münze"></div>
  <h3>Liquidität sichern<br>durch Immobilienverkauf</h3>
  <p>Wir beraten, verkaufen und wickeln zuver-<br>lässig und diskret Ihren Immobilieverkauf ab.</p>
</article>
<article class="abs card" style="left:790px">
  <div class="card-visual" role="img" aria-label="Illustration: älteres Paar mit Gehhilfen"></div>
  <h3>Immobilie im<br>Alter verkaufen</h3>
  <p>Die richtige Entscheidung treffen. Mit dem richtigen Partner eine sorgenfrei Angelegenheit.</p>
</article>

<svg class="abs cta-shape" width="1200" height="190" aria-hidden="true">
  <polygon points="533,0 1200,0 1033,185 710,185" fill="#2b3740"/>
</svg>
<h2 class="abs cta-title">JETZT TERMIN<br>VEREINBAREN!</h2>

<p class="abs intro">Unsere Experten freuen sich darauf, Sie bei Ihren Immobilienverkauf beraten und begleiten zu dürfen. Kontaktieren Sie uns gerne telefonisch oder über das folgende Kontaktformular.</p>

<div class="abs map" role="img" aria-label="Stadtplan mit Standortmarkierung">
  <svg width="291" height="320" aria-hidden="true">
    <path d="M163 62c-18 0-30 14-30 30 0 22 30 52 30 52s30-30 30-52c0-16-12-30-30-30z" fill="#7cb518"/>
    <circle cx="163" cy="91" r="11" fill="none" stroke="#fff" stroke-width="4"/>
  </svg>
</div>
<address class="abs address">
  Adresse<br>Lindenkamp 12<br>22111 Hamburg<br>Tel:&nbsp; 040 318 274 50 - 0<br>Fax: 040 318 274 60 - 1<br>URL: http://www.beispiel-stadtweb.de
</address>

<form class="abs form">
  <fieldset class="field"><legend>Name*</legend></fieldset>
  <fieldset class="field"><legend>Firmenname*</legend></fieldset>
  <fieldset class="field"><legend>Anzahl Aufträge / Positionen pro Monat*</legend></fieldset>
  <fieldset class="field"><legend>Email*</legend></fieldset>
  <fieldset class="field"><legend>Telefonnummer</legend></fieldset>
  <fieldset class="field tall"><legend>Ihre Nachricht*</legend></fieldset>
  <p class="consent">Ich stimme der Datenverarbeitung zu. Weitere Informationen<br>finden Sie in der Datenschutzerklärung.</p>
  <button class="submit" type="button">ABSENDEN</button>
</form>

<footer class="abs footer">
  <nav><a href="#">AGB</a><a href="#">Datenschutz</a><a href="#">Impressum</a><a href="#">Cookie Einstellungen</a></nav>
  <div class="copy">© 2021&nbsp; HALVAK IMMOBILIEN</div>
</footer>

</body>
</html>
```